依頼詳細
2021年11月25日から28日まで下落合のRUMBA2046で行います。

7・Marelle×FoldedMothS合併公演

題名
「灯影ノ箱」(そらごとのいろ)※ノはカタカナです。

あらすじ
彩は幸せだった。慎ましい暮らしだが、彩が幼い頃から思い焦がれていた、普通の幸せだ。
長屋の者は皆親切で、夫の玄之助は誰よりも優しい人だ。だから玄之助が友人の借金を背負ってしまった時も咎めなかった。むしろこの人らしいと、好ましくさえ思えた。
とはいえ金は返さなくてはいけない。幸い、彩は手に職があった。この時ばかりは、技術を仕込んでくれた父に感謝した。

また人を殺すのは気が重いが、この幸せを守るためなら。

こちらの公演のチラシデザインをお願いしたいです。
タイトルロゴは、可能であれば既存のフォントをそのまま使用するのではなくデザインしていただけるとありがたいです。
裏面は、情報量が多く、現時点で未確定な情報もありますので、デザイナーさんを絞ってから直接連絡させていただきます。
表面のデザインはチケット等にも使用したいと考えておりますので、タイトルロゴや文字情報とデザインを別々のデータでいただけると助かります。

表面カラー(CMYK)、裏面白黒2色です。
裏面は文字情報が多く載ります。
出演者が23人になる予定です、各出演者の写真も利用して頂きたいと考えております。

過去公演の参考です。
http://7marelle-example.com/tate/wp-content/uploads/vol11/夕霞.pdf
記載項目
タイトル 灯影ノ箱

他情報
7・Marelle×FoldedMothS合併記念公演第2弾
2021年11月25日(木)〜28日(日)
会場 下落合RUMBA2046

劇団ロゴ(添付ファイル)
サイズ
A4
ページ数
両面
希望イメージ
シンプル 複雑
単色 カラフル
暗い 明るい
日常 高級
遊び心 厳粛
未来的 伝統的
女性的 男性的
希望する色
黄・オレンジ系、青系、紫系、登場人物が色に因んた名前です、鮮やかだけどどこか寂しげな
納品ファイル
• イラストレーター形式 (.ai)
補足説明
イラストレーターのバージョンはCS2でお願いします。
メインの舞台は丘上の大きな屋敷になります。
物語のテーマとして、人の二面性、表の顔と裏の顔、嘘と真実などがあり、それを紅葉の色の変化と紐付けて表現するよていです。
上記、必ず描いて欲しいものではありませんが、イメージの参考になりましたら。
参考用の添付ファイルには画像を使用してますが今回画像は使用しない方向で考えております。

今回の公演のイメージにピッタリだったので選ばせて頂きました!

皆様素敵なデザインをありがとうございました。
とても嬉しく感謝しておりますm(_ _)m

```html
<!DOCTYPE html>
<html lang="ja">
<head>
<meta charset="utf-8">
<title>灯影ノ箱</title>
<link rel="stylesheet" href="https://fonts.googleapis.com/css2?family=Shippori+Mincho:wght@500;700&family=M+PLUS+Rounded+1c:wght@500&display=swap">
<style>
  :root {
    --paper: #fbf1e8;
    --wash-light: #f6c9a2;
    --wash-mid: #f0a064;
    --wash-deep: #e8782f;
    --ink: #1c1612;
    --accent: #c8281e;
    --line: rgba(255,255,255,0.9);
  }
  html, body { margin: 0; padding: 0; overflow: hidden; }
  .flyer {
    position: relative;
    width: 849px;
    height: 1200px;
    overflow: hidden;
    background: linear-gradient(165deg, #f4b889 0%, #f7cfae 35%, var(--paper) 80%, #ffffff 100%);
    font-family: "Shippori Mincho", serif;
    color: var(--ink);
  }
  .watercolor {
    position: absolute;
    inset: 0;
    background:
      radial-gradient(circle at 440px 570px, var(--wash-deep) 0, #ec8a45 190px, var(--wash-mid) 270px, rgba(240,160,100,0) 340px),
      radial-gradient(ellipse 520px 420px at 180px 160px, rgba(240,150,90,0.55), rgba(240,150,90,0));
  }
  .geometry {
    position: absolute;
    inset: 0;
  }
  .event-info {
    position: absolute;
    left: 22px;
    top: 36px;
    writing-mode: vertical-rl;
    font-size: 22px;
    font-weight: 500;
    letter-spacing: 0.06em;
    line-height: 1;
  }
  .event-info .label { font-size: 15px; margin-bottom: 8px; }
  .event-info .value { margin-bottom: 14px; }
  .title {
    position: absolute;
    left: 415px;
    top: 40px;
    margin: 0;
    writing-mode: vertical-rl;
    font-size: 230px;
    font-weight: 700;
    line-height: 1;
    letter-spacing: 0.06em;
  }
  .title .accent { color: var(--accent); font-weight: 500; }
  .company {
    position: absolute;
    left: 18px;
    bottom: 14px;
    display: flex;
    align-items: center;
    gap: 12px;
    font-family: "M PLUS Rounded 1c", sans-serif;
    font-weight: 500;
    font-size: 25px;
    color: var(--ink);
  }
  .company .mark {
    width: 44px;
    height: 44px;
    border-radius: 50%;
    background: var(--ink);
  }
</style>
</head>
<body>
  <main class="flyer">
    <div class="watercolor" role="img" aria-label="オレンジの水彩のにじみ、中央に濃い円形の滲み"></div>

    <svg class="geometry" width="849" height="1200" viewBox="0 0 849 1200" aria-hidden="true">
      <g fill="none" stroke="var(--line)" stroke-width="1.6">
        <polygon points="430,300 720,380 760,640 560,860 270,800 235,500"/>
        <polygon points="470,275 735,440 690,760 430,880 245,690 300,390"/>
      </g>
    </svg>

    <div class="event-info">
      <span class="label">とき</span>
      <span class="value">令和三年十一月二十五日[木]〜二十八日[日]</span>
      <span class="label">ところ</span>
      <span class="value">下落合RUMBA2046</span>
    </div>

    <h1 class="title">灯影<span class="accent">ノ</span>箱</h1>

    <div class="company">
      <span class="mark"></span>
      <span class="company-name">7・Marelle×FoldedMothS合併記念公演第2弾</span>
    </div>
  </main>
</body>
</html>
```